Consulting company needs website design

We need a simple, static website design for our consulting company. We are looking for a general design of the look and feel of the website. Initially, it will have these pages:
- Home
- About us
- Services
- Contact us
We have our own logo which I have attached to the brief.

We are looking for a simple website, with white background and the use of gray (darker) as the main theme. Simple fonts. The website should be responsive so it an be easily red in mobile devices.

As part of the project, we will need to receive at least the following items:
- Individual files with sample text to support the pages outlined above
- Necessary CSS files

Our current website is here: http://www.marlowvane.co/

Here are some examples of other website we like to be used as guideline:
- http://www.tornaviamundo.com/
-

Target Market(s)

Individuals and companies looking to hire our company to provide consulting services.

Industry/Entity Type

It Company

Coding

Coded - Design and coding required

Number of Pages Required

4 page

Font styles to use
Sans Serif

Requirements
Must have
• Main page should have the ability to embed Chirply feed into it.
• We prefer the design to use gray tones.

```html
<!DOCTYPE html>
<html lang="en">
<head>
<meta charset="utf-8">
<title>Marlow Vane Group SAS — Market Research & Consulting</title>
<link rel="stylesheet" href="https://fonts.googleapis.com/css2?family=Roboto:wght@300;400;500;700&family=Caveat:wght@400&display=swap">
<style>
:root{
  --navy:#114a6b;
  --navy-dark:#0d3d59;
  --ink:#2b2b2b;
  --text:#555b61;
  --muted:#8a9096;
  --line:#e2e4e7;
  --panel:#f4f5f7;
  --card:#f3f4f6;
  --placeholder:#b9b9b9;
  --footer:#35393e;
  --footer-text:#a9adb2;
  --white:#ffffff;
}
*{box-sizing:border-box;margin:0;padding:0}
html,body{width:1200px;height:2917px;overflow:hidden}
body{font-family:"Roboto",Arial,sans-serif;color:var(--text);background:var(--white);position:relative}
.site-header{height:68px;display:flex;align-items:center;padding:0 60px;position:relative}
.brand{display:flex;align-items:center;gap:10px;font-size:15px;line-height:17px;color:var(--text)}
.brand-mark{width:44px;height:44px;border:1.5px solid #bfc3c7;border-radius:50%}
.main-nav{position:absolute;left:428px;display:flex;gap:30px;font-size:13px;font-weight:500;color:var(--ink)}
.hero{height:467px;position:relative;text-align:center;color:var(--white);background:linear-gradient(180deg,#2e8fbd 0%,#1f7fb1 55%,#2b8cbb 100%)}
.hero-title{font-family:"Caveat",cursive;font-weight:400;font-size:66px;line-height:88px;padding-top:70px;letter-spacing:2px}
.hero-sub{font-size:21px;line-height:27px;font-weight:500;margin-top:20px}
.hero-actions{display:flex;justify-content:center;gap:36px;margin-top:32px}
.btn{display:inline-block;font-size:10px;font-weight:700;padding:9px 14px;border-radius:2px}
.btn-light{background:var(--white);color:var(--navy)}
.btn-outline{border:1.5px solid var(--white);color:var(--white)}
.hero-dots{position:absolute;bottom:28px;left:0;right:0;display:flex;justify-content:center;gap:8px}
.hero-dots span{width:9px;height:9px;border-radius:50%;background:rgba(255,255,255,.6)}
.hero-dots span:first-child{background:var(--white)}
.stats{height:249px;display:flex;padding:0 51px;overflow:hidden}
.stat{flex:1;text-align:center;padding:10px 22px 0}
.stat h3{font-size:19px;font-weight:400;color:var(--ink)}
.stat strong{display:block;font-size:46px;font-weight:500;color:var(--navy);margin:14px 0 26px}
.stat p{font-size:12.5px;line-height:20px}
.about{height:387px;background:var(--panel);padding:0 40px;border-bottom:3px solid #d8dbde}
.section-title{font-size:22px;font-weight:500;color:var(--ink);text-align:center;padding-top:24px;padding-bottom:14px;border-bottom:1px solid var(--line)}
.pillars{display:flex;padding-top:42px}
.pillar{flex:1;text-align:center;padding:0 18px}
.pillar-icon{width:76px;height:80px;margin:0 auto;background:var(--navy);display:flex;align-items:center;justify-content:center}
.pillar h4{font-size:18px;font-weight:500;color:var(--ink);margin:18px 0 18px}
.pillar p{font-size:12.5px;line-height:20px}
.banner{height:276px;background:radial-gradient(ellipse at 55% 60%,#2d4c86 0%,#17295a 55%,#0f1c40 100%)}
.services{height:520px;padding:0 51px;overflow:hidden}
.services .section-title{padding-top:22px;padding-bottom:12px;border-color:var(--line)}
.services-body{display:flex;gap:34px;padding-top:34px}
.services-art{width:533px;height:400px;flex:none;background:linear-gradient(180deg,#ffffff 0%,#d5e2ee 60%,#b8cee2 100%)}
.service-list{list-style:none;margin-top:-12px}
.service-list li{display:flex;align-items:center;gap:14px;height:55px;font-size:16px;color:var(--ink)}
.chev{width:22px;height:22px;border:1px solid var(--line);display:flex;align-items:center;justify-content:center}
.news{height:536px;padding:0 51px}
.news .section-title{padding-top:0;padding-bottom:14px}
.news-grid{display:flex;gap:28px;padding-top:32px}
.news-card{width:254px;background:var(--card)}
.news-thumb{height:186px;background:var(--placeholder);display:flex;align-items:center;justify-content:center;font-size:32px;color:#222}
.news-body{padding:14px 16px 0;height:168px;position:relative}
.news-body h5{font-size:17px;font-weight:700;color:var(--ink);margin-bottom:10px}
.news-body p{font-size:12.5px;line-height:19px}
.news-meta{position:absolute;left:16px;right:16px;bottom:16px;border-top:1px solid var(--line);padding-top:14px;display:flex;justify-content:space-between;font-size:11px}
.news-more{text-align:center;padding-top:46px}
.btn-dark{background:var(--navy-dark);color:var(--white);font-size:12px;padding:11px 20px}
.site-footer{height:418px;background:var(--footer);color:var(--footer-text);padding:52px 51px 0;position:relative}
.footer-cols{display:flex}
.footer-col{width:282px;font-size:12.5px;line-height:20px;padding-right:20px}
.footer-col h6{font-size:18px;font-weight:500;color:var(--white);margin-bottom:20px}
.footer-col p{margin-bottom:12px}
.footer-col .label{color:var(--white)}
.social{display:flex;gap:12px;margin-top:4px}
.social span{width:12px;height:12px;border-radius:50%;background:var(--footer-text)}
.post{display:flex;align-items:center;gap:16px;margin-bottom:22px}
.post-thumb{width:48px;height:48px;border-radius:50%;background:#c9c9c9;color:#333;font-size:9px;display:flex;align-items:center;justify-content:center;flex:none}
.post b{display:block;font-weight:400;color:var(--white);font-size:12.5px}
.post small{font-size:10.5px}
.quote{display:flex;gap:14px}
.quote-mark{font-size:56px;line-height:42px;color:#7d8287;font-family:Georgia,serif}
.reviewer{display:flex;align-items:center;gap:18px;margin-top:22px}
.reviewer-photo{width:80px;height:80px;border-radius:50%;background:#c9c9c9;color:#333;font-size:12px;display:flex;align-items:center;justify-content:center}
.reviewer b{display:block;color:var(--white);font-weight:400;font-size:15px}
.footer-bottom{position:absolute;left:51px;right:51px;bottom:0;height:66px;border-top:1px solid #464a50;font-size:11.5px;padding-top:26px}
</style>
</head>
<body>
<header class="site-header">
  <div class="brand"><span class="brand-mark"></span><span>Marlow Vane<br>Group SAS</span></div>
  <nav class="main-nav"><span>HOME</span><span>ABOUT US</span><span>SERVICES</span><span>CONTACT US</span></nav>
</header>

<section class="hero" role="img" aria-label="Photo of a team working at laptops, tinted blue, behind the welcome message">
  <h1 class="hero-title">Welcome to<br>Marlow Vane Group SAS</h1>
  <p class="hero-sub">Your trusted market research provider, dedicated to the<br>provision of meaningful and actionable insights</p>
  <div class="hero-actions"><span class="btn btn-light">ABOUT US</span><span class="btn btn-outline">GO ON SURFING</span></div>
  <div class="hero-dots"><span></span><span></span><span></span><span></span></div>
</section>

<section class="stats">
  <div class="stat"><h3>Interviews in 2015</h3><strong>87000 +</strong><p>Marlow Vane Group's experience and partnerships across all regions and sectors in US has enabled the company to complete projects of various sizes and specifications while maintaining high levels of efficiency and quality</p></div>
  <div class="stat"><h3>Satisfied Clients</h3><strong>100 +</strong><p>Given their satisfaction with our work, the majority of the clients have become our partners they turn to us as year after year with their research problems</p></div>
  <div class="stat"><h3>Finished Projects</h3><strong>240 +</strong><p>Major sponsors of Marlow Vane Group work have included government and public sector organizations, foundations and associations, international and local organizations, and private sector entities</p></div>
</section>

<section class="about">
  <h2 class="section-title">Partners &amp; Consulting Analysis</h2>
  <div class="pillars">
    <div class="pillar">
      <div class="pillar-icon"><svg width="38" height="38" viewBox="0 0 24 24" fill="none" stroke="#fff" stroke-width="1.5"><path d="M7 10v11H3V10zM7 20h10.5a2 2 0 0 0 2-1.6l1.3-6A2 2 0 0 0 18.8 10H14V5a2 2 0 0 0-2-2l-5 7"/></svg></div>
      <h4>Who we are</h4>
      <p>The quality perception of the product, what clients would like to change, what price can they afford, where is this product wanted the most, what causes dissatisfaction in a product (i.e. price, quality,design)</p>
    </div>
    <div class="pillar">
      <div class="pillar-icon"><svg width="38" height="38" viewBox="0 0 24 24" fill="none" stroke="#fff" stroke-width="1.5"><path d="M12 2c3 3 4 7 3 12H9C8 9 9 5 12 2z"/><circle cx="12" cy="9" r="1.5"/><path d="M9 14l-3 3 3 0M15 14l3 3-3 0M11 18v3M13 18v3"/></svg></div>
      <h4>Our Mission</h4>
      <p>Marlow Vane Group is a team of research professionals that work toward delivering research services while upholding the highest standards of design, analysis and reporting. Our mission is to help set the industry in consulting services</p>
    </div>
    <div class="pillar">
      <div class="pillar-icon"><svg width="34" height="38" viewBox="0 0 20 24" fill="none" stroke="#fff" stroke-width="1.5"><path d="M3 2h10l4 4v16H3z"/><path d="M6 10h8M6 14h8M6 18h5"/></svg></div>
      <h4>Our Vision</h4>
      <p>Our vision is to be a long-term preferred partner to our clients in the field of market research and business consulting. We are relentlessly focused on delivering exceptional value in provision of strategy, research and analysis</p>
    </div>
  </div>
</section>

<section class="banner" role="img" aria-label="Dark blue chalk-style banner with sketches of management, organization, vision and growth over a world map"></section>

<section class="services">
  <h2 class="section-title">What We Do</h2>
  <div class="services-body">
    <div class="services-art" role="img" aria-label="Flat illustration of consultants working at laptops in front of a city skyline and wall charts"></div>
    <ul class="service-list">
      <li><span class="chev"><svg width="10" height="6" viewBox="0 0 10 6"><path d="M1 1l4 4 4-4" fill="none" stroke="#777" stroke-width="1.4"/></svg></span>Business Strategy</li>
      <li><span class="chev"><svg width="10" height="6" viewBox="0 0 10 6"><path d="M1 1l4 4 4-4" fill="none" stroke="#777" stroke-width="1.4"/></svg></span>Executive Coaching</li>
      <li><span class="chev"><svg width="10" height="6" viewBox="0 0 10 6"><path d="M1 1l4 4 4-4" fill="none" stroke="#777" stroke-width="1.4"/></svg></span>Corporate Governance</li>
      <li><span class="chev"><svg width="10" height="6" viewBox="0 0 10 6"><path d="M1 1l4 4 4-4" fill="none" stroke="#777" stroke-width="1.4"/></svg></span>Performance Management</li>
      <li><span class="chev"><svg width="10" height="6" viewBox="0 0 10 6"><path d="M1 1l4 4 4-4" fill="none" stroke="#777" stroke-width="1.4"/></svg></span>Interim Management of Special Projects</li>
      <li><span class="chev"><svg width="10" height="6" viewBox="0 0 10 6"><path d="M1 1l4 4 4-4" fill="none" stroke="#777" stroke-width="1.4"/></svg></span>New Business Development</li>
      <li><span class="chev"><svg width="10" height="6" viewBox="0 0 10 6"><path d="M1 1l4 4 4-4" fill="none" stroke="#777" stroke-width="1.4"/></svg></span>Risk Management</li>
      <li><span class="chev"><svg width="10" height="6" viewBox="0 0 10 6"><path d="M1 1l4 4 4-4" fill="none" stroke="#777" stroke-width="1.4"/></svg></span>Financial Management</li>
    </ul>
  </div>
</section>

<section class="news">
  <h2 class="section-title">Latest News</h2>
  <div class="news-grid">
    <article class="news-card"><div class="news-thumb">270x200</div><div class="news-body"><h5>Ullamcorper Parturien</h5><p>Morbi leo risus, porta ac consectur at eros. Maecenas sed diam eget risus varius blandit sit amet non.</p><div class="news-meta"><span>28 October, 2020</span><span>15</span></div></div></article>
    <article class="news-card"><div class="news-thumb">270x200</div><div class="news-body"><h5>Excepteur Sint Occaecat</h5><p>Lorem ipsum dolor sit amet, consectetur adipiscing elit, sed do eiusmod tempor incididunt ut lab.</p><div class="news-meta"><span>27 October, 2020</span><span>11</span></div></div></article>
    <article class="news-card"><div class="news-thumb">270x200</div><div class="news-body"><h5>Neque Porro Quisquam</h5><p>Sed ut perspiciatis unde omnis iste natus error sit voluptatem accusantium doloremque laudanti.</p><div class="news-meta"><span>26 October, 2020</span><span>10</span></div></div></article>
    <article class="news-card"><div class="news-thumb">270x200</div><div class="news-body"><h5>Quis Autem Vel Eum</h5><p>Nemo enim ipsam voluptatem quia voluptas sit aspernatur aut odit aut fugit, sed quia consetur.</p><div class="news-meta"><span>25 October, 2020</span><span>15</span></div></div></article>
  </div>
  <div class="news-more"><span class="btn btn-dark">VIEW MORE</span></div>
</section>

<footer class="site-footer">
  <div class="footer-cols">
    <div class="footer-col">
      <h6>Contact Us</h6>
      <p>Maecenas etos sit amet, consectetur adipiscing elit. Terminal volutpat rutrum metro amet sollicitudin interdum.</p>
      <p><span class="label">Phone:</span> +1 (800) 555 01 42</p>
      <p><span class="label">Office:</span> 418 Alder Lane, New York</p>
      <p><span class="label">Email:</span> info@marlowvane.co</p>
      <div class="social"><span></span><span></span><span></span><span></span><span></span></div>
    </div>
    <div class="footer-col">
      <h6>Recent Posts</h6>
      <div class="post"><span class="post-thumb">50x50</span><div><b>Business Cards Design Trends</b><small>Dec 02, 2020 / 2 comments</small></div></div>
      <div class="post"><span class="post-thumb">50x50</span><div><b>This Maravelous App</b><small>Nov 18, 2020 / 9 comments</small></div></div>
      <div class="post"><span class="post-thumb">50x50</span><div><b>Brand Paper Niceties</b><small>Nov 10, 2020 / 0 comments</small></div></div>
    </div>
    <div class="footer-col"><h6>Latest Twitts</h6></div>
    <div class="footer-col">
      <h6>Last Review</h6>
      <div class="quote"><span class="quote-mark">&ldquo;</span><p>Lorem ipsum dolor sit amet, consectetur adipiscing elit, sed do eiusmod tempor incididunt ut labore et dolore magna aliqua. Ut enim ad minim veniam, quis nostrud exercitation ullamco.</p></div>
      <div class="reviewer"><span class="reviewer-photo">84x84</span><div><b>Dana Whitlow</b><small>Creative Designer</small></div></div>
    </div>
  </div>
  <div class="footer-bottom">Copyright 2020. All Rights Reserved by Marlow Vane Group</div>
</footer>
</body>
</html>
```